Business Card Design

My husband & I have a singing business so just need a card with my husband's photo on it and our current logo. I have attached the logo on the top of a page plus a photo of my husband & our theme colour we would like is a black background with red writing to match our logo. If you can please also put somewhere on the card "Entertainment for any occasion inc. Pubs, Clubs, Birthday Parties or Weddings". The photo is on the poster attached if you are able to copy it please.

Industry/Entity Type

Business

Contact Information for Business Card

Rocco & Jen Farley
Mobile: 0498 362 514
Email: janice.brook@mailnest.example

```html
<!DOCTYPE html>
<html lang="en">
<head>
<meta charset="utf-8">
<title>Encore Duo Entertainment – Business Card</title>
<link rel="stylesheet" href="https://fonts.googleapis.com/css2?family=Oswald:wght@400;700&family=Lobster&display=swap">
<style>
  :root {
    --page-bg: #ececec;
    --card-black: #000000;
    --logo-panel: #1b1b1b;
    --brand-red: #e3141b;
    --band-red: #e0131a;
    --photo-border: #d8161c;
    --text-white: #ffffff;
    --tagline-ink: #1a0a0a;
  }
  * { box-sizing: border-box; margin: 0; padding: 0; }
  html, body {
    width: 1200px;
    height: 993px;
    overflow: hidden;
    background: var(--page-bg);
  }
  .card {
    position: absolute;
    left: 75px;
    top: 196px;
    width: 1050px;
    height: 600px;
    background: var(--card-black);
    box-shadow: 0 6px 24px rgba(0,0,0,0.18);
    overflow: hidden;
  }
  .logo-panel {
    position: absolute;
    left: 290px;
    top: 80px;
    width: 470px;
    height: 200px;
    background: var(--logo-panel);
    display: flex;
    flex-direction: column;
    justify-content: center;
    padding-left: 40px;
  }
  .logo-name {
    font-family: "Oswald", sans-serif;
    font-weight: 700;
    color: var(--brand-red);
    font-size: 56px;
    line-height: 1.05;
    letter-spacing: 0.5px;
  }
  .logo-sub {
    font-family: "Oswald", sans-serif;
    font-weight: 700;
    color: var(--brand-red);
    font-size: 40px;
    line-height: 1.1;
  }
  .logo-sub small {
    font-size: 13px;
    vertical-align: middle;
    margin-left: 6px;
  }
  .contact-name {
    position: absolute;
    left: 400px;
    top: 280px;
    font-family: "Oswald", sans-serif;
    font-weight: 700;
    font-size: 36px;
    color: var(--brand-red);
    text-transform: uppercase;
    letter-spacing: 0.5px;
  }
  .portrait {
    position: absolute;
    left: 290px;
    top: 335px;
    width: 108px;
    height: 122px;
    border: 3px solid var(--photo-border);
    background: linear-gradient(160deg, #f3e6d8 0%, #b57a55 50%, #3a2a22 100%);
  }
  .contact-line {
    position: absolute;
    left: 412px;
    display: flex;
    align-items: center;
    gap: 12px;
    font-family: "Lobster", cursive;
    font-size: 26px;
    color: var(--text-white);
  }
  .contact-line.phone { top: 350px; }
  .contact-line.email { top: 398px; }
  .contact-line svg { width: 26px; height: 26px; flex: none; }
  .tagline-band {
    position: absolute;
    left: 0;
    top: 478px;
    width: 100%;
    height: 42px;
    background: var(--band-red);
    display: flex;
    align-items: center;
    justify-content: center;
    font-family: "Lobster", cursive;
    font-size: 21px;
    color: var(--tagline-ink);
    letter-spacing: 0.3px;
  }
</style>
</head>
<body>
  <div class="card">
    <div class="logo-panel">
      <div class="logo-name">Encore Duo</div>
      <div class="logo-sub">Entertainment<small>PTY LTD</small></div>
    </div>

    <div class="contact-name">Rocco &amp; Jen Farley</div>

    <div class="portrait" role="img" aria-label="Portrait photo of the singer"></div>

    <div class="contact-line phone">
      <svg viewBox="0 0 26 26" aria-hidden="true">
        <circle cx="13" cy="13" r="12" fill="#ffffff"/>
        <rect x="9" y="6" width="8" height="14" rx="1.5" fill="#000"/>
        <rect x="10.3" y="8" width="5.4" height="8.5" fill="#fff"/>
        <circle cx="13" cy="18.2" r="0.9" fill="#fff"/>
      </svg>
      <span>0498 362 514</span>
    </div>

    <div class="contact-line email">
      <svg viewBox="0 0 26 26" aria-hidden="true">
        <circle cx="13" cy="13" r="12" fill="#ffffff"/>
        <rect x="6.5" y="8.5" width="13" height="9" fill="none" stroke="#000" stroke-width="1.5"/>
        <polyline points="6.5,8.5 13,14 19.5,8.5" fill="none" stroke="#000" stroke-width="1.5"/>
      </svg>
      <span>janice.brook@mailnest.example</span>
    </div>

    <div class="tagline-band">" Entertainment for any occasion inc. Pubs, Clubs, Birthday Parties or Weddings"</div>
  </div>
</body>
</html>
```